Design Labels and Brand Look For Mens Soap Company

We are developing a mens soap line for a natural body wash and exfoliating bar. We will be selling this with our line of mens toiletry bags that we sell under the name of Corvane Totes on Quillmart. We are looking for you to design the product brand look with brand color palette and fonts.

The title for the mens body was is "Body Wash For Men". The title for the soap bar is "Exfoliating Bar Soap For Men"

We are providing the templates for these 2 items in PDF form. The final version of the design needs to be in a layered PSD format. You also need to send us the fonts used.

This soap will be sold on Quillmart. Do a search for "men's body wash" and "mens soap bar" you will see our competition on page one. We need to stand out with colors and design differentiaon.

Target Market(s)

Men

Industry/Entity Type

Skin Care Product

Requirements
Must have
• Layered PSD file with all fonts

```html
<!DOCTYPE html>
<html lang="en">
<head>
<meta charset="utf-8">
<title>Corvane Body Wash For Men – Label</title>
<link rel="stylesheet" href="https://fonts.googleapis.com/css2?family=Questrial&family=Kaushan+Script&family=Cinzel:wght@900&display=swap">
<style>
  :root {
    --lime: #9fd400;
    --leaf: #5f9a12;
    --forest: #1d3a1a;
    --night: #0f1a20;
    --ink: #111111;
    --paper: #ffffff;
    --trim: #e0126e;
    --bleed: #2bb4e6;
    --legal-red: #e3103a;
    --mist: #e4ecf2;
    --badge-light: #d6e6a6;
    --badge-deep: #a9c768;
  }
  * { margin: 0; padding: 0; box-sizing: border-box; }
  html, body { width: 1200px; height: 653px; overflow: hidden; background: var(--paper); }
  .label {
    position: relative; width: 1200px; height: 653px; overflow: hidden;
    font-family: "Questrial", sans-serif; color: var(--ink);
  }
  .bleed-edge {
    position: absolute; left: 8px; top: 10px; width: 1182px; height: 634px;
    border: 1px solid var(--bleed);
    background: linear-gradient(180deg, var(--lime) 0%, #8cc000 22%, var(--leaf) 38%, var(--forest) 50%, var(--night) 60%, var(--night) 100%);
  }
  .scene {
    position: absolute; left: 152px; top: 56px; width: 834px; height: 555px;
  }
  .safe-line {
    position: absolute; left: 31px; top: 33px; width: 1140px; height: 590px;
    border: 1.5px dashed var(--ink); border-radius: 8px;
  }
  .trim-line {
    position: absolute; left: 39px; top: 42px; width: 1121px; height: 569px;
    border: 1px solid var(--trim);
  }
  .panel { position: absolute; background: var(--paper); }
  .panel--legal { left: 35px; top: 37px; width: 117px; height: 574px; }
  .panel--info { left: 986px; top: 42px; width: 174px; height: 569px; }

  .legal-text {
    position: absolute; left: 14px; top: 0; width: 110px; height: 574px;
    writing-mode: vertical-rl; text-align: center;
    font-size: 19px; line-height: 25.5px; letter-spacing: 1.2px;
    display: flex; flex-direction: column; justify-content: center;
  }
  .legal-text .placeholder { color: var(--legal-red); }
  .legal-text .origin { color: var(--ink); letter-spacing: 2px; }

  .info-text {
    position: absolute; left: 10px; top: 10px; width: 154px; height: 550px;
    writing-mode: vertical-rl; transform: rotate(180deg);
    font-size: 16px; line-height: 20.5px; letter-spacing: 0.4px;
  }
  .info-text p { text-align: justify; text-align-last: left; }
  .info-text .directions { margin-left: 10px; }
  .info-text .flag { color: var(--legal-red); }

  .brand-badge {
    position: absolute; left: 434px; top: 67px; width: 247px; height: 180px;
    border: 4px solid var(--ink); border-radius: 50%;
    background: radial-gradient(ellipse at 50% 35%, var(--badge-light) 0%, var(--badge-deep) 100%);
    display: flex; align-items: center; justify-content: center;
  }
  .brand-name {
    font-family: "Questrial", sans-serif; font-size: 46px; color: var(--ink);
    letter-spacing: 1px;
  }

  .title {
    position: absolute; left: 317px; top: 366px; width: 480px; text-align: center;
    font-weight: normal;
  }
  .title-script {
    font-family: "Kaushan Script", cursive; font-size: 88px; line-height: 92px;
    color: var(--ink);
    text-shadow: 2px 2px 0 var(--paper), -2px -2px 0 var(--paper), 2px -2px 0 var(--paper), -2px 2px 0 var(--paper);
  }
  .title-sub {
    position: absolute; left: 442px; top: 452px; display: flex; align-items: baseline;
  }
  .title-for {
    font-family: "Kaushan Script", cursive; font-size: 32px; color: var(--ink);
    margin-right: 2px;
    text-shadow: 1.5px 1.5px 0 var(--paper), -1.5px -1.5px 0 var(--paper), 1.5px -1.5px 0 var(--paper), -1.5px 1.5px 0 var(--paper);
  }
  .title-men {
    font-family: "Cinzel", serif; font-weight: 900; font-size: 78px; line-height: 78px; color: var(--ink);
    text-shadow: 2px 2px 0 var(--paper), -2px -2px 0 var(--paper), 2px -2px 0 var(--paper), -2px 2px 0 var(--paper);
  }
  .title-men .small { font-size: 62px; }

  .volume {
    position: absolute; left: 476px; top: 544px; width: 164px; height: 27px;
    border-radius: 14px; background: var(--mist);
    font-size: 18px; line-height: 27px; text-align: center; color: var(--ink);
  }
</style>
</head>
<body>
<main class="label">
  <div class="bleed-edge"></div>

  <svg class="scene" role="img" aria-label="Waterfall cascading over grey rocks, framed by bright green leaves and ferns" viewBox="0 0 834 555">
    <defs>
      <radialGradient id="water" cx="50%" cy="62%" r="45%">
        <stop offset="0%" stop-color="#eef4f8"/>
        <stop offset="45%" stop-color="#c7d6e0" stop-opacity="0.95"/>
        <stop offset="80%" stop-color="#5d7482" stop-opacity="0.5"/>
        <stop offset="100%" stop-color="#0f1a20" stop-opacity="0"/>
      </radialGradient>
      <linearGradient id="foliage" x1="0" x2="1">
        <stop offset="0%" stop-color="#3f7d1a" stop-opacity="0.85"/>
        <stop offset="30%" stop-color="#8fd22a" stop-opacity="0"/>
        <stop offset="70%" stop-color="#8fd22a" stop-opacity="0"/>
        <stop offset="100%" stop-color="#3f7d1a" stop-opacity="0.85"/>
      </linearGradient>
    </defs>
    <rect width="834" height="555" fill="url(#water)"/>
    <rect y="150" width="834" height="405" fill="url(#foliage)"/>
  </svg>

  <div class="safe-line"></div>
  <div class="trim-line"></div>

  <aside class="panel panel--legal">
    <div class="legal-text">
      <span class="placeholder">[business name &amp; contact information</span>
      <span class="placeholder">(incl. address with zip code &amp; telephone number)]</span>
      <span class="origin">MADE IN USA</span>
    </div>
  </aside>

  <aside class="panel panel--info">
    <div class="info-text">
      <p class="directions">Pour a small amount of our luxurious hand soap into the palm of your hands and rub together under water for a rich, cleansing lather.</p>
      <p class="ingredients">Contains: Water, Sodium Laureth Sulfate, Vegetable Glycerine, <span class="flag">ADDITIVES</span>, Sodium Chloride, Fragrance, Citric Acid, Sodium Benzoate, Potassium Sorbate, Vitamin E, Cocoa Butter, Shea Butter, Virgin Olive Oil, Grapeseed Oil, <span class="flag">COLORS</span>.</p>
    </div>
  </aside>

  <div class="brand-badge"><span class="brand-name">Corvane</span></div>

  <h1 class="title"><span class="title-script">Body Wash</span></h1>
  <div class="title-sub">
    <span class="title-for">For</span>
    <span class="title-men">M<span class="small">EN</span></span>
  </div>

  <div class="volume">16 FL OZ (473 mL)</div>
</main>
</body>
</html>
```